Stationery Design Project

Would like to have the design elements we created in for our website (www.brook-holdings.example), incorporated in a stationery design layout.
Updates
Colors used in the logo attachments do not need to be used. We are open to different color variations. Looking for a crisp, clean, modern update using the design elements in attachments and which can also be viewed on or website.
A note to designers:
Project Deadline Extended
Reason: Due to update in our project description and requirements, we have decided to extend the deadline of this project to provide ample opportunity to all designers participating .
Requirements
Must have
- Must have continuity with the theme and design features used in our website. Have attached .jpg images of some of the design elements.

```html
<!DOCTYPE html>
<html lang="en">
<head>
<meta charset="utf-8">
<title>Brook Holdings Letterhead</title>
<link rel="stylesheet" href="https://fonts.googleapis.com/css2?family=Open+Sans:wght@400;700&display=swap">
<style>
  :root {
    --backdrop: #e9e6e2;
    --paper: #ffffff;
    --ink: #1f1f1f;
    --rule-green: #6fb33f;
    --rule-blue: #2f6fb0;
    --mark-grey: #555555;
    --faint-grey: #e2e2e2;
  }
  * { margin: 0; padding: 0; box-sizing: border-box; }
  html, body {
    width: 1200px;
    height: 900px;
    overflow: hidden;
    background: var(--backdrop);
    font-family: "Open Sans", Arial, sans-serif;
    color: var(--ink);
  }
  .canvas {
    width: 1200px;
    height: 900px;
    display: flex;
    align-items: center;
    justify-content: center;
  }
  .letterhead {
    position: relative;
    width: 594px;
    height: 840px;
    background: var(--paper);
    box-shadow: 0 4px 18px rgba(0, 0, 0, 0.18);
  }
  .letterhead-header {
    position: absolute;
    top: 34px;
    left: 34px;
    right: 34px;
    height: 62px;
  }
  .company-block {
    position: absolute;
    left: 0;
    top: 0;
    padding-right: 14px;
    border-right: 1.5px solid var(--ink);
    font-size: 11px;
    font-weight: 700;
    line-height: 1.4;
  }
  .company-block p { margin: 0; }
  .brand-name {
    position: absolute;
    right: 6px;
    bottom: 8px;
    font-size: 18px;
    font-weight: 400;
    color: var(--mark-grey);
    letter-spacing: 0.5px;
  }
  .brand-dot {
    display: inline-block;
    width: 8px;
    height: 8px;
    border-radius: 50%;
    background: var(--mark-grey);
    margin-left: 6px;
    vertical-align: middle;
  }
  .gradient-rule {
    position: absolute;
    left: 0;
    right: 0;
    height: 3px;
    background: linear-gradient(90deg, var(--rule-green), var(--rule-blue));
  }
  .gradient-rule.top { top: 100px; }
  .gradient-rule.bottom { bottom: 24px; }
  .watermark-name {
    position: absolute;
    left: 40px;
    bottom: 95px;
    font-size: 118px;
    font-weight: 400;
    color: var(--faint-grey);
    letter-spacing: 2px;
    line-height: 1;
  }
  .contact-line {
    position: absolute;
    left: 34px;
    bottom: 36px;
    font-size: 9.5px;
    font-weight: 700;
    letter-spacing: 0.2px;
  }
</style>
</head>
<body>
  <main class="canvas">
    <section class="letterhead">
      <header class="letterhead-header">
        <div class="company-block">
          <p>Brook Holdings, Inc.</p>
          <p>48 Alder Lane Suite 120</p>
          <p>Fairview, GA 30000</p>
        </div>
        <div class="brand-name">Brook<span class="brand-dot"></span></div>
      </header>
      <div class="gradient-rule top"></div>

      <div class="watermark-name" aria-hidden="true">Brook</div>

      <footer class="contact-line">
        PHONE: (555) 014-2277, FAX: (555) 014-3390, E-mail us: info@brook-holdings.example
      </footer>
      <div class="gradient-rule bottom"></div>
    </section>
  </main>
</body>
</html>
```